Real Estate Seller Financing Postcard

I need a postcard that lays out these options contained in the notes that grabs attention, explains the two options easily and is eye-catching. The front needs to have the percentages on it and information about it and on the other side One side exact Text is:
"Monthly income without tenant headaches" in big letters. Also on front "Get
110%
add an "or"
160% of market value for your property. ". The percentages should be displayed and that is not to be a sentence of text. Other side text: I need bullets points for these "Formal protection as a lien holder against home
No commission or closing cost
Fast closings possible
Property taken as is so no repairs.

Add to the top of the back in "It’s simple. I am a new investor without down payment capital who still want to double our portfolio this year to grow our portfolio."
Here are the two options that are to be the largest part of the back
Option 1, you can receive 80% now cash and 30% over a short period of time including interest.

Option 2, where act like a bank allowing you to make 150% if you finance the whole property(ies). No gimmicks and surprises, just simple unconventional financing.

Include Logo Somewhere

Target Market(s)

Property Owners Wanting to Sell Their Property

Industry/Entity Type

Real Estate Investing

Requirements
Must have
• The options promiment and each side with its respective information. Must have logo somewhere
Nice to have
• The options in color other than black.
Should not have
• A picture of money on the front. Any other image is okay.

```html
<!DOCTYPE html>
<html lang="en">
<head>
<meta charset="utf-8">
<title>Harbor Crest Property Group – Seller Financing Postcard</title>
<link href="https://fonts.googleapis.com/css2?family=Montserrat:wght@600;700;800;900&family=Lexend:wght@300;400;500;600&family=Space+Grotesk:wght@500;700&display=swap" rel="stylesheet">
<style>
:root{
  --navy:#1f3f8f;
  --navy-dark:#1d3366;
  --blue:#2a4ea0;
  --sky:#27a6e0;
  --green:#5cb86a;
  --grey-tab:#8a8c8f;
  --ink:#111;
  --muted:#8d8f93;
  --stage:#a9aaae;
  --panel:#f1f2f4;
}
*{margin:0;padding:0;box-sizing:border-box}
html,body{width:849px;height:1200px;overflow:hidden}
body{background:var(--stage);font-family:"Lexend",sans-serif;position:relative}
.card{position:absolute;left:35px;width:776px;height:517px;background:var(--navy);}
.card-front{top:62px}
.card-back{top:634px}
.abs{position:absolute}

/* front */
.hero-photo{left:10px;top:10px;width:756px;height:260px;background:linear-gradient(100deg,#3f5ea6 0%,#6b83bd 45%,#9fb0cf 70%,#b8c4d6 100%)}
.title-plate{left:0;top:0}
.title-monthly{left:32px;top:58px;font-family:"Montserrat",sans-serif;font-weight:900;font-size:58px;letter-spacing:1px;color:#fff;text-shadow:3px 3px 0 var(--sky);line-height:1}
.title-income{left:30px;top:128px;font-family:"Montserrat",sans-serif;font-weight:900;font-size:100px;color:#fff;text-shadow:4px 4px 0 var(--sky);line-height:1}
.title-sub{left:34px;top:227px;font-family:"Montserrat",sans-serif;font-weight:800;font-size:24px;letter-spacing:1.6px;color:#fff}
.front-white{left:10px;top:270px;width:526px;height:238px;background:#fff}
.people-frame{left:536px;top:185px;width:230px;height:148px;background:#fff}
.people-photo{left:552px;top:195px;width:205px;height:118px;background:linear-gradient(90deg,#6f7c8d,#c8bfb6 55%,#ece8e3)}
.offer{left:28px;top:279px;height:43px;display:flex;align-items:center;font-family:"Space Grotesk",sans-serif}
.pct{height:43px;display:flex;align-items:center;color:#fff;font-weight:700;font-size:30px;padding:0 22px 0 8px;clip-path:polygon(0 0,100% 0,88% 100%,0 100%)}
.pct-green{background:var(--green);width:170px}
.pct-blue{background:var(--sky);width:116px;padding-left:22px;clip-path:polygon(12% 0,100% 0,88% 100%,0 100%)}
.or{font-family:"Montserrat",sans-serif;font-weight:700;font-size:17px;margin:0 8px 0 0;color:var(--ink)}
.offer-note{margin-left:12px;font-weight:700;font-size:16px;letter-spacing:1.5px;line-height:21px;color:var(--ink)}
.chart{left:27px;top:335px;width:498px;height:104px}
.brand{display:flex;align-items:center;gap:8px}
.brand-mark{border-radius:50%;border:2px solid var(--navy)}
.brand-name{font-family:"Montserrat",sans-serif;font-weight:700;color:var(--navy);line-height:1}
.front-brand{left:40px;top:454px}
.front-brand .brand-mark{width:40px;height:40px}
.front-brand .brand-name{font-size:15px;width:150px}
.phone{display:flex;align-items:center;gap:18px;font-family:"Montserrat",sans-serif;font-weight:800;color:var(--navy)}
.front-phone{left:234px;top:455px;font-size:31px}
.benefits{left:536px;top:331px;width:230px;height:177px;background:#fff}
.benefit{display:flex;align-items:center;gap:14px;height:44px;padding-left:15px;font-size:13.5px;line-height:17px;color:var(--ink)}
.benefit.is-band{background:var(--navy);color:#fff;clip-path:polygon(0 0,100% 0,96% 100%,0 100%)}
.tick{width:13px;height:13px;flex:none}

/* back */
.back-top{left:10px;top:10px;width:756px;height:139px;background:#fff}
.house-photo{left:532px;top:10px;width:234px;height:139px;background:linear-gradient(180deg,#dfeaf3 0%,#c9d3db 45%,#8aa36a 75%,#6aa33c 100%)}
.quote-mark{font-family:"Montserrat",sans-serif;color:#d3d5d9;font-size:32px;font-weight:800}
.simple-title{left:55px;top:56px;font-family:"Montserrat",sans-serif;font-weight:800;font-size:31px;color:var(--navy);letter-spacing:-0.5px}
.simple-body{left:55px;top:101px;font-weight:600;font-size:13.6px;line-height:18.5px;color:var(--ink)}
.option{top:148px;height:180px;background:linear-gradient(120deg,#fff 0%,var(--panel) 100%)}
.option-1{left:10px;width:362px}
.option-2{left:377px;width:389px}
.tab{position:absolute;left:0;top:0;height:46px;display:flex;align-items:center;padding-left:33px;font-family:"Montserrat",sans-serif;font-weight:700;font-size:20px;color:#fff;letter-spacing:.5px}
.tab-1{width:176px;background:var(--navy);clip-path:polygon(0 0,100% 0,82% 100%,0 100%)}
.tab-2{width:176px;background:var(--grey-tab);padding-left:30px;clip-path:polygon(0 0,100% 0,82% 100%,0 100%)}
.tab-lead{position:absolute;top:14px;font-weight:600;font-size:19px;color:var(--navy)}
.option-1 .tab-lead{left:180px}
.option-2 .tab-lead{left:185px}
.option-body{position:absolute;left:34px;color:var(--ink)}
.option-1 .option-body{top:66px}
.option-2 .option-body{top:60px;left:18px}
.big-claim{font-family:"Montserrat",sans-serif;font-weight:900;font-size:32px;letter-spacing:-.3px;line-height:1.1}
.option-text{font-size:17.5px;line-height:24px;margin-top:8px}
.option-text strong{font-weight:600}
.finance-line{font-weight:600;font-size:17.5px;line-height:26px}
.finance-line .big-claim{font-size:31px}
.fine-print{font-weight:300;font-size:14.5px;line-height:19px;color:var(--muted);margin-top:10px}
.back-bottom{left:10px;top:333px;width:756px;height:175px;background:#fff}
.cta{left:38px;top:333px;width:311px;height:57px;background:var(--navy-dark);color:#fff;font-family:"Montserrat",sans-serif;font-weight:700;font-size:22px;display:flex;align-items:center;justify-content:center;letter-spacing:.5px}
.back-brand{left:55px;top:405px}
.back-brand .brand-mark{width:62px;height:62px}
.back-brand .brand-name{font-size:22px;width:220px}
.back-phone{left:385px;top:366px;font-size:37px;gap:24px}
.email{left:384px;top:422px;display:flex;align-items:center;gap:18px;font-size:20px;letter-spacing:1px;color:var(--navy)}
</style>
</head>
<body>

<section class="card card-front" aria-label="Postcard front">
  <div class="abs hero-photo" role="img" aria-label="Photo of a two-storey house with grey siding and a tiled roof under a blue sky"></div>
  <svg class="abs title-plate" width="776" height="330" viewBox="0 0 776 330" aria-hidden="true">
    <polygon points="22,53 404,53 380,123 490,123 490,262 10,262 10,53" fill="var(--navy)"/>
  </svg>
  <div class="abs title-monthly">MONTHLY</div>
  <div class="abs title-income">INCOME</div>
  <div class="abs title-sub">WITHOUT TENANT HEADACHES</div>

  <div class="abs front-white"></div>
  <div class="abs people-frame"></div>
  <div class="abs people-photo" role="img" aria-label="Photo of a homeowner greeting a visitor at her front door"></div>

  <div class="abs offer">
    <div class="pct pct-green">Get 110%</div>
    <div class="or">OR</div>
    <div class="pct pct-blue">160%</div>
    <div class="offer-note">of market value<br>for your property</div>
  </div>

  <svg class="abs chart" viewBox="0 0 498 104" aria-label="Rising value chart from 10% to 160%">
    <defs><linearGradient id="chartBg" x1="0" x2="1"><stop offset="0" stop-color="#22409a"/><stop offset="1" stop-color="#1e4894"/></linearGradient></defs>
    <rect width="498" height="104" fill="url(#chartBg)"/>
    <g font-family="Montserrat, sans-serif" font-weight="700" font-size="7" fill="#fff">
      <text x="37" y="26">10%</text><text x="69" y="26">20%</text><text x="104" y="26">40%</text>
      <text x="138" y="26">60%</text><text x="171" y="26">80%</text><text x="202" y="26">100%</text>
      <text x="237" y="26">110%</text><text x="270" y="26">120%</text><text x="304" y="26">140%</text><text x="339" y="26">160%</text>
    </g>
    <g stroke="#3b5db0" stroke-width="0.6">
      <line x1="24" y1="34" x2="24" y2="104"/><line x1="84" y1="34" x2="84" y2="104"/><line x1="144" y1="34" x2="144" y2="104"/>
      <line x1="204" y1="34" x2="204" y2="104"/><line x1="264" y1="34" x2="264" y2="104"/><line x1="324" y1="34" x2="324" y2="104"/>
      <line x1="384" y1="34" x2="384" y2="104"/>
      <line x1="0" y1="104" x2="498" y2="104"/>
    </g>
    <polyline points="24,41 245,59 24,84" fill="none" stroke="#5cb86a" stroke-width="0.7"/>
    <polyline points="24,50 350,59 24,92" fill="none" stroke="#27a6e0" stroke-width="0.7"/>
    <polyline points="390,84 410,58 420,68 440,36" fill="none" stroke="#5cb86a" stroke-width="4" stroke-linecap="round"/>
    <polygon points="446,28 432,34 444,42" fill="#5cb86a"/>
    <polyline points="400,72 420,48 432,72 452,44 462,62 480,22" fill="none" stroke="#27a6e0" stroke-width="5" stroke-linecap="round" stroke-linejoin="round"/>
    <polygon points="484,10 470,22 488,28" fill="#27a6e0"/>
  </svg>

  <div class="abs brand front-brand">
    <span class="brand-mark"></span>
    <span class="brand-name">HARBOR CREST PROPERTY GROUP</span>
  </div>

  <div class="abs phone front-phone">
    <svg width="26" height="26" viewBox="0 0 24 24" aria-hidden="true"><path fill="var(--navy)" d="M6.6 10.8c1.4 2.8 3.8 5.1 6.6 6.6l2.2-2.2c.3-.3.7-.4 1-.2 1.1.4 2.3.6 3.6.6.6 0 1 .4 1 1V20c0 .6-.4 1-1 1C10.6 21 3 13.4 3 4c0-.6.4-1 1-1h3.5c.6 0 1 .4 1 1 0 1.3.2 2.5.6 3.6.1.3 0 .7-.2 1z"/><path d="M14 3a7 7 0 0 1 7 7M14 6.5a3.5 3.5 0 0 1 3.5 3.5" fill="none" stroke="var(--navy)" stroke-width="1.8" stroke-linecap="round"/></svg>
    <span>+1 555 014 2277</span>
  </div>

  <ul class="abs benefits">
    <li class="benefit is-band"><svg class="tick" viewBox="0 0 16 16" aria-hidden="true"><circle cx="8" cy="8" r="8" fill="#fff"/><path d="M4.5 8.2l2.4 2.3 4.6-4.8" fill="none" stroke="var(--navy)" stroke-width="2"/></svg>Fast closings possible</li>
    <li class="benefit"><svg class="tick" viewBox="0 0 16 16" aria-hidden="true"><circle cx="8" cy="8" r="8" fill="var(--navy)"/><path d="M4.5 8.2l2.4 2.3 4.6-4.8" fill="none" stroke="#fff" stroke-width="2"/></svg>Formal protection as a lien holder against home</li>
    <li class="benefit is-band"><svg class="tick" viewBox="0 0 16 16" aria-hidden="true"><circle cx="8" cy="8" r="8" fill="#fff"/><path d="M4.5 8.2l2.4 2.3 4.6-4.8" fill="none" stroke="var(--navy)" stroke-width="2"/></svg>No commission or closing cost</li>
    <li class="benefit"><svg class="tick" viewBox="0 0 16 16" aria-hidden="true"><circle cx="8" cy="8" r="8" fill="var(--navy)"/><path d="M4.5 8.2l2.4 2.3 4.6-4.8" fill="none" stroke="#fff" stroke-width="2"/></svg>Property taken as is so no repairs.</li>
  </ul>
</section>

<section class="card card-back" aria-label="Postcard back">
  <div class="abs back-top"></div>
  <div class="abs house-photo" role="img" aria-label="Photo of a single-storey modern home with a patio and green lawn"></div>
  <div class="abs quote-mark" style="left:22px;top:50px">“</div>
  <h1 class="abs simple-title">It’s Simple.</h1>
  <p class="abs simple-body">I am a new investor without down payment capital who still<br>want to double our portfolio this year to grow our portfolio. <span class="quote-mark" style="font-size:20px">”</span></p>

  <div class="abs option option-1">
    <div class="tab tab-1">OPTION 1</div>
    <div class="tab-lead">You can receive</div>
    <div class="option-body">
      <div class="big-claim">80% NOW CASH</div>
      <p class="option-text">and <strong>30% over a short period</strong> of<br>time including interest.</p>
    </div>
  </div>

  <div class="abs option option-2">
    <div class="tab tab-2">OPTION 2</div>
    <div class="tab-lead">We act like a bank</div>
    <div class="option-body">
      <p class="finance-line">allowing you to <span class="big-claim">MAKE 150%</span><br>if you finance the whole property(ies)</p>
      <p class="fine-print">No gimmicks and surprises, just simple<br>unconventional financing.</p>
    </div>
  </div>

  <div class="abs back-bottom"></div>
  <div class="abs cta">CONTACT US TODAY!</div>
  <div class="abs brand back-brand">
    <span class="brand-mark"></span>
    <span class="brand-name">HARBOR CREST PROPERTY GROUP</span>
  </div>
  <div class="abs phone back-phone">
    <svg width="24" height="24" viewBox="0 0 24 24" aria-hidden="true"><path fill="var(--navy)" d="M6.6 10.8c1.4 2.8 3.8 5.1 6.6 6.6l2.2-2.2c.3-.3.7-.4 1-.2 1.1.4 2.3.6 3.6.6.6 0 1 .4 1 1V20c0 .6-.4 1-1 1C10.6 21 3 13.4 3 4c0-.6.4-1 1-1h3.5c.6 0 1 .4 1 1 0 1.3.2 2.5.6 3.6.1.3 0 .7-.2 1z"/><path d="M14 3a7 7 0 0 1 7 7M14 6.5a3.5 3.5 0 0 1 3.5 3.5" fill="none" stroke="var(--navy)" stroke-width="1.8" stroke-linecap="round"/></svg>
    <span>+1 555 014 2277</span>
  </div>
  <div class="abs email">
    <svg width="28" height="20" viewBox="0 0 28 20" aria-hidden="true"><rect x="1" y="1" width="26" height="18" fill="none" stroke="var(--navy)" stroke-width="2"/><path d="M1 1l13 10L27 1M1 19l10-9M27 19l-10-9" fill="none" stroke="var(--navy)" stroke-width="2"/></svg>
    <span>hello@harborcrest.example</span>
  </div>
</section>

</body>
</html>
```